Cash Balance Retirement Plan Services Page

We are looking to have a services/landing page created for one of our offerings. The goal of the page is to explain a relatively complex service (advanced retirement plan) by highlighting the benefits and uses for the plan such that it tells a story that encourages individuals and businesses that would benefit from the plans to reach out.

The page will be used both as a landing page (though secondarily) and as a page that many of our partners will show to their clients in order to generate interest. We help other people closes these deals so we want it to handle both.

Overall, we would want the page to incorporate the following sections/areas.
1. Headline and a place for a video at the top
2. Explanation of what a cash balance plan is (a paragraph or two)
3. These five benefits: These are the 7 we usually use, but only include five at a time so only need room for five.
a. Highest Tax Deductible Contributions Allowed
b. Significantly reduce your taxes
c. Potential Negative “Net Cost”
d. Owner & Executive Weighted Benefits
e. Retain and Attract Top Talen
f. Catch Up On decades of low retirement savings in a matter of years
g. Potential for life time income
4. A section comparing the contribution limits allowed for each plan type (Please see attached image as an example).
5. A place for a table of contribution amounts (This will just be an image. Also, attached).
6. A place for a compare table
6. Who should consider such a plan
7. Occasional banners for call to actions
8. FAQ

Our primary audience for this project are successful small business owners with a particular focus on medical professionals (doctors, chiropractors, dentists, plastic surgeons, etc.). In generally, they will be between 45 and 65 years old and earn $150k or more.

Because we work a lot with financial, business strategy, and insurance based products that require a significant investment by the client trust, professionalism, and sophistication are important attributes we wish to portray in the design of the page. Our preferred colors are blue or green. Though we are still working on figuring out the color scheme so your input as a designer is welcomed as your creativity can help us communicate the attributes we seek to embody for our clients.

In the attached document, I have included some additional information about the service itself if it helps to have some context, as well as a more flushed out outline of the details above.

Importantly, I am not a marketer so any creative input is always welcome if there is a best practice we are not incorporating in either our design requests or outline.

Here is the URL for our current page: https://www.tidewellpro.com/physicianreserve

Please don't let this page be your muse. We're trying to get away from it for a reason :) But it still will hopefully provide some helpful information, copy examples, and context.

Additionally, please don't feel like you need to read the full cash balance explanation. That's only if context will be helpful.

We are also going through a rebranding so please don't rely on the colors from the TidewellPro logo you may see on the website. I've attached two sample logos for the rebrand for context.

```html
<!DOCTYPE html>
<html lang="en">
<head>
<meta charset="utf-8">
<title>Cash Balance Plan | Summit Ridge Financial</title>
<link href="https://fonts.googleapis.com/css2?family=Montserrat:wght@500;600;700;800&family=Mulish:wght@400;600;700;800&family=Lato:wght@400;700&display=swap" rel="stylesheet">
<style>
:root{
  --navy:#134a86;
  --navy-deep:#0d3a73;
  --blue:#1d5fb4;
  --ink:#222a33;
  --text:#3b4250;
  --muted:#5d6472;
  --light:#eef1f5;
  --grey-band:#e9ecf0;
  --card:#ffffff;
  --faq-a:#0e3a8e;
  --faq-b:#1652b8;
  --footer:#2a2b2e;
  --green-a:#7cc242;
  --green-b:#1fa34a;
  --sky:#8bbcef;
  --bar-blue:#1660d1;
}
*{box-sizing:border-box;margin:0;padding:0}
html,body{width:1200px;height:4874px;overflow:hidden}
body{position:relative;background:#fff;font-family:"Mulish",sans-serif;color:var(--text)}
.abs{position:absolute}
/* header */
.site-header{position:absolute;left:0;top:0;width:1200px;height:80px;background:#fff}
.brand{position:absolute;left:132px;top:22px;display:flex;align-items:center;gap:10px}
.brand-dot{width:36px;height:36px;border-radius:50%;background:var(--navy)}
.brand-name{font-family:"Montserrat",sans-serif;font-weight:800;font-size:15px;line-height:16px;color:var(--navy);width:120px;text-transform:uppercase}
.main-nav{position:absolute;left:394px;top:24px;display:flex;gap:0;font-family:"Montserrat",sans-serif;font-weight:600;font-size:13px;color:var(--ink)}
.main-nav a{display:block;padding:6px 10px;margin-right:14px;color:var(--ink);text-decoration:none}
.main-nav a.active{border:2px solid var(--navy);color:var(--navy);padding:4px 8px}
.call{position:absolute;left:914px;top:22px;display:flex;align-items:center;gap:10px}
.call-icon{width:30px;height:30px;border-radius:50%;background:var(--navy);display:flex;align-items:center;justify-content:center}
.call-text{font-family:"Montserrat",sans-serif;font-size:10px;font-weight:600;color:var(--ink);line-height:13px}
.call-text b{display:block;font-size:13px;color:var(--navy);font-weight:700}
/* hero */
.hero{position:absolute;left:0;top:80px;width:1200px;height:600px;overflow:hidden}
.hero-photo{position:absolute;inset:0;background:linear-gradient(100deg,#3f4d5c 0%,#6e7f90 35%,#aab8c6 60%,#d9dfe6 80%,#b9c4cf 100%)}
.hero-shade{position:absolute;inset:0;background:linear-gradient(90deg,rgba(20,30,45,.55) 0%,rgba(20,30,45,.25) 45%,rgba(0,0,0,0) 70%)}
.hero-tag{position:absolute;left:132px;top:104px;border:2px solid #fff;color:#fff;font-family:"Montserrat",sans-serif;font-weight:600;font-size:22px;padding:4px 12px;letter-spacing:.5px}
.hero-title{position:absolute;left:130px;top:162px;width:420px;color:#fff;font-family:"Montserrat",sans-serif;font-weight:800;font-size:38px;line-height:45px;text-transform:uppercase}
.hero-btn{position:absolute;left:132px;top:365px;width:167px;height:49px;border:2px solid #fff;background:var(--navy);color:#fff;font-family:"Montserrat",sans-serif;font-weight:700;font-size:15px;display:flex;align-items:center;justify-content:center}
.play{position:absolute;left:558px;top:194px;width:96px;height:96px}
.hero-wave{position:absolute;left:0;bottom:-2px;width:1200px;height:70px}
/* what is */
.what-photo{position:absolute;left:0;top:680px;width:644px;height:503px;background:linear-gradient(120deg,#dfe4ea 0%,#b7c2ce 40%,#7c8fa6 70%,#c9d2dc 100%)}
.section-title{font-family:"Montserrat",sans-serif;font-weight:700;font-size:19px;color:var(--navy);text-transform:uppercase;letter-spacing:.2px}
.section-title .dark{color:var(--ink)}
.what-copy{position:absolute;left:706px;top:700px;width:370px}
.what-copy p{font-size:13.5px;line-height:22.5px;color:var(--text);margin-top:36px}
.ticks{list-style:none;margin-top:22px}
.ticks li{font-size:13.5px;line-height:25px;color:var(--text);padding-left:18px;position:relative}
.ticks li::before{content:"";position:absolute;left:2px;top:8px;border-left:6px solid var(--navy);border-top:4.5px solid transparent;border-bottom:4.5px solid transparent}
.ticks b{color:var(--blue)}
.pill-btn{position:absolute;left:706px;top:1077px;width:332px;height:68px;border-radius:34px;background:var(--navy);color:#fff;font-family:"Montserrat",sans-serif;font-weight:700;font-size:14.5px;line-height:22px;padding:13px 0 0 28px}
/* why */
.why{position:absolute;left:0;top:1183px;width:1200px;height:1090px;background:linear-gradient(180deg,#e6eaef 0%,#f3f5f7 40%,#e9edf1 100%)}
.center-title{position:absolute;left:0;width:1200px;text-align:center}
.rule{position:absolute;left:585px;width:30px;height:3px;background:var(--navy)}
.card{position:absolute;width:282px;height:398px;background:var(--card);border-radius:14px;text-align:center;box-shadow:0 6px 24px rgba(20,40,70,.08)}
.card.featured{background:var(--navy);color:#fff;box-shadow:0 10px 30px rgba(10,40,90,.35)}
.card .icon{width:124px;height:124px;margin:30px auto 0;border-radius:50%;background:#d6e4f3;display:flex;align-items:center;justify-content:center}
.card .icon span{width:96px;height:96px;border-radius:50%;background:var(--navy);display:flex;align-items:center;justify-content:center}
.card.featured .icon{background:rgba(255,255,255,.25)}
.card.featured .icon span{background:#fff}
.card h3{font-family:"Montserrat",sans-serif;font-weight:700;font-size:16.5px;line-height:23px;color:var(--ink);margin-top:24px;padding:0 20px}
.card.featured h3{color:#fff}
.card p{font-size:11.5px;line-height:17px;color:var(--text);margin-top:14px;padding:0 26px}
.card p+p{margin-top:14px}
.card.featured p{color:#e5ecf6}
.card .story{position:absolute;left:79px;bottom:30px;width:124px;height:40px;border:2px solid var(--navy);border-radius:20px;font-family:"Montserrat",sans-serif;font-weight:700;font-size:13px;color:var(--navy);display:flex;align-items:center;justify-content:center;background:#fff}
.card.featured .story{border-color:#fff}
.cta-pill{position:absolute;left:405px;top:971px;width:415px;height:50px;border-radius:25px;background:var(--navy);color:#fff;font-family:"Montserrat",sans-serif;font-weight:700;font-size:15px;display:flex;align-items:center;justify-content:center}
.why-wave{position:absolute;left:0;top:1060px;width:1200px;height:40px}
/* table */
.contrib{position:absolute;left:199px;top:2451px;width:799px;border-collapse:collapse;font-family:"Lato",sans-serif;box-shadow:0 2px 6px rgba(0,0,0,.25);border:4px solid #fff}
.contrib th{background:var(--navy-deep);color:#fff;font-size:19px;font-weight:700;text-align:left;vertical-align:top;padding:6px 8px;line-height:27px;border-right:2px solid #fff;height:119px}
.contrib td{font-size:19px;color:#111;padding:0 8px;height:36px;border-right:2px solid #fff;border-top:1px solid #fff}
.contrib tr:nth-child(odd) td{background:#c9d2ec}
.contrib tr:nth-child(even) td{background:#e3e8f4}
.contrib td.bold{font-weight:700}
/* chart */
.chart-band{position:absolute;left:0;top:2820px;width:1200px;height:570px;background:linear-gradient(180deg,#eceef1 0%,#f7f8f9 100%)}
.chart-text{position:absolute;font-family:Arial,Helvetica,sans-serif;font-weight:700;font-size:17px;color:#111;text-align:center;line-height:20px}
.bar{position:absolute}
.chart-note{position:absolute;left:888px;top:3003px;width:100px;font-family:Arial,Helvetica,sans-serif;font-size:14.5px;line-height:17px;color:#111;text-align:center}
/* who */
.who-copy{position:absolute;left:132px;top:3460px;width:436px}
.who-copy p{font-size:13.5px;line-height:22.5px;color:var(--text);margin-top:34px}
.criteria{position:absolute;left:132px;top:3634px;width:436px;height:313px;background:#eff0f2;padding:26px 22px}
.criteria li{list-style:none;position:relative;padding-left:26px;font-size:11.5px;line-height:17px;color:var(--text);margin-bottom:22px}
.criteria li::before{content:"";position:absolute;left:0;top:2px;width:11px;height:11px;border-radius:50%;background:var(--navy)}
.who-cta{position:absolute;left:132px;top:3960px;width:436px;height:91px;background:var(--navy);color:#fff;font-family:"Montserrat",sans-serif;font-weight:700;font-size:14.5px;line-height:22px;padding:12px 22px}
.who-cta .no{color:#9fc8f5;font-size:22px}
.who-photo{position:absolute;left:606px;top:3464px;width:464px;height:587px;background:linear-gradient(180deg,#b9cde0 0%,#8fa9c4 45%,#3b4b5f 100%)}
/* faq */
.faq{position:absolute;left:0;top:4089px;width:1200px;height:540px;background:linear-gradient(180deg,var(--faq-a) 0%,var(--faq-b) 100%);overflow:hidden}
.faq h2{position:absolute;left:0;top:36px;width:1200px;text-align:center;font-family:"Montserrat",sans-serif;font-weight:700;font-size:19px;color:#fff}
.faq .rule{background:#fff;top:70px}
.faq-item{position:absolute;left:341px;width:520px;height:48px;border-bottom:2px solid rgba(255,255,255,.85);color:#fff;font-size:15.5px}
.faq-item span{position:absolute;left:0;top:8px}
.faq-item svg{position:absolute;right:10px;top:8px}
/* footer */
.site-footer{position:absolute;left:0;top:4560px;width:1200px;height:314px}
.footer-brand{position:absolute;left:132px;top:4680px;display:flex;align-items:center;gap:14px}
.footer-brand .brand-dot{width:66px;height:66px;background:#4a4f57}
.footer-brand .brand-name{font-size:28px;line-height:30px;width:220px;color:#5a8fd6}
.follow{position:absolute;left:837px;top:4688px;font-family:"Montserrat",sans-serif;font-size:10px;font-weight:600;color:#fff;letter-spacing:.3px}
.social{position:absolute;top:4675px;width:34px;height:34px;border-radius:50%;background:var(--blue)}
.foot-nav{position:absolute;left:577px;top:4738px;display:flex;gap:24px;font-family:"Montserrat",sans-serif;font-size:12.5px;font-weight:500;color:#fff;text-transform:uppercase}
.foot-line{position:absolute;left:0;top:4798px;width:1200px;height:1px;background:rgba(255,255,255,.15)}
.copyright{position:absolute;left:0;top:4825px;width:1200px;text-align:center;font-size:11.5px;color:#fff}
</style>
</head>
<body>

<header class="site-header">
  <div class="brand"><span class="brand-dot"></span><span class="brand-name">Summit Ridge Financial</span></div>
  <nav class="main-nav">
    <a class="active">HOME</a><a>ABOUT US</a><a>BENEFITS</a><a>PLAN</a><a>FAQ</a><a>CONTACT US</a>
  </nav>
  <div class="call">
    <span class="call-icon"><svg width="14" height="14" viewBox="0 0 24 24"><path fill="#fff" d="M6.6 10.8a15 15 0 0 0 6.6 6.6l2.2-2.2a1 1 0 0 1 1-.25 11.4 11.4 0 0 0 3.6.57 1 1 0 0 1 1 1V20a1 1 0 0 1-1 1A17 17 0 0 1 3 4a1 1 0 0 1 1-1h3.5a1 1 0 0 1 1 1c0 1.25.2 2.45.57 3.57a1 1 0 0 1-.25 1z"/></svg></span>
    <div class="call-text">CALL US<b>+1 800 555 0142</b></div>
  </div>
</header>

<section class="hero">
  <div class="hero-photo" role="img" aria-label="Smiling doctor in a white coat holding a tablet in a bright clinic"></div>
  <div class="hero-shade"></div>
  <div class="hero-tag">WELCOME TO</div>
  <h1 class="hero-title">Maximize your deductions while securing your retirement</h1>
  <div class="hero-btn">WATCH VIDEO</div>
  <svg class="play" viewBox="0 0 96 96"><circle cx="48" cy="48" r="45" fill="none" stroke="#fff" stroke-width="3"/><circle cx="48" cy="48" r="36" fill="#fff"/><path d="M40 33 L64 48 L40 63 Z" fill="#5b6470"/></svg>
  <svg class="hero-wave" viewBox="0 0 1200 70" preserveAspectRatio="none"><path d="M0 45 C300 0 700 5 1200 0 L1200 70 L0 70Z" fill="#fff"/><path d="M0 45 C300 0 700 5 1200 0 L1200 12 C700 18 300 15 0 60Z" fill="var(--navy)"/></svg>
</section>

<div class="what-photo" role="img" aria-label="Smiling businessman in a light blue suit in an office"></div>
<div class="what-copy">
  <h2 class="section-title">What <span class="dark">is a Cash-Balance Plan</span></h2>
  <p>A cash balance plan is a retirement plan specifically for small business owners, doctors, lawyers, and other high-income professionals. It allows for the highest tax-deductible contribution limits in the market, and the older you get, the higher those limits go. You then get an option for guaranteed income for life or a one time, lump payout.</p>
  <ul class="ticks">
    <li>Up to <b>$160k</b> saved on taxes</li>
    <li>Up to <b>$417k</b> annual contributions</li>
    <li>Up to <b>$2.9M</b> retirement benefit</li>
    <li>Risk of Outliving Your Retirement Savings</li>
  </ul>
</div>
<div class="pill-btn">How much can you save?<br>Download Max Contribution Table</div>

<section class="why">
  <h2 class="section-title center-title" style="top:38px">Why a Cash Balance Plan</h2>
  <div class="rule" style="top:78px"></div>

  <div class="card" style="left:144px;top:119px">
    <div class="icon"><span><svg width="44" height="50" viewBox="0 0 44 50"><rect x="4" y="2" width="32" height="44" rx="3" fill="none" stroke="#fff" stroke-width="3"/><path d="M11 14h18M11 22h18M11 30h12" stroke="#fff" stroke-width="3"/></svg></span></div>
    <h3>Highest Tax Deductible Contributions Allowed</h3>
    <p>Most retirement plans in the US (IRAs, 401(k), SEP) allow $7k, $27k, or $61k .</p>
    <p>Mark caught up on decades of low retirement savings</p>
    <div class="story">HIS STORY</div>
  </div>
  <div class="card featured" style="left:458px;top:119px">
    <div class="icon"><span><svg width="44" height="50" viewBox="0 0 44 50"><path d="M14 12 C4 22 4 46 22 46 C40 46 40 22 30 12Z" fill="none" stroke="var(--navy)" stroke-width="3"/><path d="M14 4h16l-4 8h-8z" fill="none" stroke="var(--navy)" stroke-width="3"/><text x="22" y="38" font-family="Arial" font-weight="700" font-size="18" fill="var(--navy)" text-anchor="middle">$</text></svg></span></div>
    <h3>Potential Negative<br>“Net Cost”</h3>
    <p>Many businesses are unable to contribute to their own retirement because .</p>
    <p>Mark caught up on decades of low retirement savings</p>
    <div class="story">HIS STORY</div>
  </div>
  <div class="card" style="left:772px;top:119px">
    <div class="icon"><span><svg width="50" height="50" viewBox="0 0 50 50"><circle cx="25" cy="14" r="8" fill="none" stroke="#fff" stroke-width="3"/><circle cx="10" cy="26" r="5" fill="none" stroke="#fff" stroke-width="3"/><circle cx="40" cy="26" r="5" fill="none" stroke="#fff" stroke-width="3"/><path d="M12 46 C14 34 36 34 38 46" fill="none" stroke="#fff" stroke-width="3"/></svg></span></div>
    <h3>Owner &amp; Executive Weighted Benefits</h3>
    <p>These plans allow greater contribution for owners and executives.</p>
    <p>Mark caught up on decades of low retirement savings</p>
    <div class="story">HIS STORY</div>
  </div>
  <div class="card" style="left:303px;top:540px">
    <div class="icon"><span><svg width="50" height="50" viewBox="0 0 50 50"><circle cx="20" cy="20" r="14" fill="none" stroke="#fff" stroke-width="3"/><text x="20" y="27" font-family="Arial" font-weight="700" font-size="18" fill="#fff" text-anchor="middle">$</text><path d="M32 46v-8M38 46v-12M44 46v-16" stroke="#fff" stroke-width="3"/></svg></span></div>
    <h3>Retain and Attract<br>Top Talen</h3>
    <p>These plans—on top of all the benefits provided the business owners or doctors.</p>
    <p>Mark caught up on decades of low retirement savings</p>
    <div class="story">HIS STORY</div>
  </div>
  <div class="card" style="left:615px;top:540px">
    <div class="icon"><span><svg width="50" height="50" viewBox="0 0 50 50"><path d="M8 44V34M18 44V28M28 44V22M38 44V14" stroke="#fff" stroke-width="5"/><path d="M6 26 L20 16 L28 20 L42 6" fill="none" stroke="#fff" stroke-width="3"/></svg></span></div>
    <h3>Potential for lifetime<br>income</h3>
    <p>These plans come with the option to receive guaranteed income for life.</p>
    <p>Mark caught up on decades of low retirement savings</p>
    <div class="story">HIS STORY</div>
  </div>
  <div class="cta-pill">What’s your story? Talk to an expert to find out</div>
  <svg class="why-wave" viewBox="0 0 1200 40" preserveAspectRatio="none"><path d="M0 20 C300 40 700 40 1200 0 L1200 40 L0 40Z" fill="#fff"/><path d="M0 20 C300 40 700 40 1200 0 L1200 10 C700 48 300 48 0 30Z" fill="var(--navy)"/></svg>
</section>

<h2 class="section-title center-title" style="top:2368px">Allowable Tax-Deductible Contribution by Age</h2>
<div class="rule" style="top:2412px"></div>
<table class="contrib">
  <thead><tr>
    <th style="width:134px">Starting<br>Plan at Age:</th>
    <th style="width:133px">Max<br>Monthly<br>Retirement<br>Benefit:</th>
    <th style="width:133px">Lump Sum<br>at<br>Retirement:</th>
    <th style="width:146px">Illustrative<br>Contribution<br>Limits:</th>
    <th style="width:119px">Estimated<br>Tax<br>Savings:</th>
    <th>“Net Cost”<br>after Tax<br>Savings:</th>
  </tr></thead>
  <tbody>
    <tr><td>40</td><td>$20,417</td><td>$2,959,124</td><td class="bold">$141,358</td><td>$56,543</td><td>$84,814</td></tr>
    <tr><td>45</td><td>$20,417</td><td>$2,959,124</td><td class="bold">$178,753</td><td>$71,501</td><td>$107,252</td></tr>
    <tr><td>50</td><td>$20,417</td><td>$2,959,124</td><td class="bold">$246,962</td><td>$98,784</td><td>$148,177</td></tr>
    <tr><td>55</td><td>$20,417</td><td>$2,959,124</td><td class="bold">$382,181</td><td>$152,872</td><td>$229,308</td></tr>
    <tr><td>60</td><td>$10,208</td><td>$1,479,561</td><td class="bold">$400,418</td><td>$160,192</td><td>$240,225</td></tr>
  </tbody>
</table>

<section class="chart-band">
  <h2 class="section-title center-title" style="top:46px">Plan Contribution Limits Comparable</h2>
  <svg class="abs" style="left:0;top:540px" width="1200" height="34" viewBox="0 0 1200 34" preserveAspectRatio="none"><path d="M0 20 C300 0 800 0 1200 4 L1200 34 L0 34Z" fill="#fff"/><path d="M0 20 C300 0 800 0 1200 4 L1200 14 C800 10 300 12 0 30Z" fill="var(--navy)"/></svg>
</section>
<div class="chart-text" style="left:212px;top:3137px;width:92px">Annual Contributions<br>Limits</div>
<div class="chart-text" style="left:318px;top:3154px;width:100px">$6,000<br>($7000)</div>
<div class="bar" style="left:333px;top:3195px;width:68px;height:19px;background:var(--green-a)"></div>
<div class="chart-text" style="left:318px;top:3225px;width:100px">IRA</div>
<div class="chart-text" style="left:466px;top:3132px;width:100px">$20,500<br>($27,000)</div>
<div class="bar" style="left:483px;top:3176px;width:66px;height:38px;background:var(--green-b)"></div>
<div class="chart-text" style="left:466px;top:3225px;width:100px">401(k)</div>
<div class="chart-text" style="left:612px;top:3098px;width:100px">$61,000</div>
<div class="bar" style="left:628px;top:3123px;width:69px;height:91px;background:var(--sky)"></div>
<div class="chart-text" style="left:622px;top:3225px;width:80px">Profit Sharin<br>g</div>
<div class="chart-text" style="left:760px;top:2946px;width:100px">$416,000</div>
<div class="bar" style="left:776px;top:2972px;width:68px;height:242px;background:var(--bar-blue)"></div>
<div class="chart-text" style="left:770px;top:3225px;width:80px">Cash Balance<br>Plan</div>
<div class="chart-note">*Your contribution limits will be based on age and salary and may not reach the max contribution amount.</div>

<div class="who-copy">
  <h2 class="section-title">Who should consider such a plan</h2>
  <p>You should learn about your options with a Cash Balance Plan design if you are a high earning executive, partner, doctor, or successful business owner and meet the following criteria:</p>
</div>
<ul class="criteria">
  <li>You are looking to maximize your tax deductions.</li>
  <li>Your income pushes you beyond the contribution limits of the lower retirement plans such as 401(k)s, SEPs or profit sharing plans.</li>
  <li>You are in your 40s, 50s, or 60s and don’t want the “2nd best” plan.</li>
  <li>You want an option to GUARANTEE a retirement benefit.</li>
  <li>You are looking for a way to “catch-up” on retirement savings that provides massive tax savings.</li>
</ul>
<div class="who-cta">Have questions before you make a decision? Don’t make an uneducated decision to say <span class="no">“no.”</span> Talk to an expert to learn what your story might be.</div>
<div class="who-photo" role="img" aria-label="Confident businessman in a navy suit with arms crossed"></div>

<section class="faq">
  <h2>FAQ</h2>
  <div class="rule"></div>
  <div class="faq-item" style="top:120px"><span>Lorem Ipsum is simply dummy text of the printing ?</span><svg width="22" height="22" viewBox="0 0 22 22"><circle cx="11" cy="11" r="9.5" fill="none" stroke="#fff" stroke-width="1.5"/><path d="M7 9l4 4 4-4" fill="none" stroke="#fff" stroke-width="1.5"/></svg></div>
  <div class="faq-item" style="top:188px"><span>There are many variations of passages of Lorem?</span><svg width="22" height="22" viewBox="0 0 22 22"><circle cx="11" cy="11" r="9.5" fill="none" stroke="#fff" stroke-width="1.5"/><path d="M7 9l4 4 4-4" fill="none" stroke="#fff" stroke-width="1.5"/></svg></div>
  <div class="faq-item" style="top:254px"><span>Contrary to popular belief, Lorem Ipsum?</span><svg width="22" height="22" viewBox="0 0 22 22"><circle cx="11" cy="11" r="9.5" fill="none" stroke="#fff" stroke-width="1.5"/><path d="M7 9l4 4 4-4" fill="none" stroke="#fff" stroke-width="1.5"/></svg></div>
  <div class="faq-item" style="top:322px"><span>It is a long established fact that a reader will be ?</span><svg width="22" height="22" viewBox="0 0 22 22"><circle cx="11" cy="11" r="9.5" fill="none" stroke="#fff" stroke-width="1.5"/><path d="M7 9l4 4 4-4" fill="none" stroke="#fff" stroke-width="1.5"/></svg></div>
  <div class="faq-item" style="top:390px"><span>Sed ut perspiciatis unde omnis iste natus error ?</span><svg width="22" height="22" viewBox="0 0 22 22"><circle cx="11" cy="11" r="9.5" fill="none" stroke="#fff" stroke-width="1.5"/><path d="M7 9l4 4 4-4" fill="none" stroke="#fff" stroke-width="1.5"/></svg></div>
</section>

<footer class="site-footer">
  <svg width="1200" height="314" viewBox="0 0 1200 314" preserveAspectRatio="none"><path d="M0 40 C400 40 900 30 1200 0 L1200 314 L0 314Z" fill="var(--footer)"/></svg>
</footer>
<div class="footer-brand"><span class="brand-dot"></span><span class="brand-name">Summit Ridge Financial</span></div>
<div class="follow">FOLLOW US</div>
<span class="social" style="left:926px"></span>
<span class="social" style="left:979px"></span>
<span class="social" style="left:1032px"></span>
<nav class="foot-nav"><span>Home</span><span>About Us</span><span>Benefits</span><span>Plan</span><span>FAQ</span><span>Contact Us</span></nav>
<div class="foot-line"></div>
<div class="copyright">Copyright © 2022 All Rights Reserved</div>

</body>
</html>
```